Business Card Design

I am an Event and Wedding Planner in need of an eye catching business card featuring my logo (attached), my contact details, and my company tagline (Making each one of your gatherings radiant...) I would like the tagline in font similar the logo's font.
Updates
I have just noticed that my logo has a misspelling so for the final design, I will be uploading a corrected logo as soon as I have it.
My apologies.
Reason: Waiting on a corrected logo...Occasions is misspelled and it should say Weddings not Wedding
The logo has been corrected so now Occasions is spelled correctly and it says Weddings instead of Wedding. Please use Edwardian Script ITC as the font for the tagline so it will match the logo. Thank you for your patience.
Target Market(s)
Engaged couples and people hosting milestone celebrations. 25-50 years old, predominately female
Industry/Entity Type
Business
Contact Information for Business Card
Delphine Marsh, Event Manager / Owner, Mobile: 0491 836 254, Email: delphine@radiantgatheringsco.com.au, www.radiantgatheringsco.com.au, Making each one of your gatherings radiant...

```html
<!DOCTYPE html>
<html lang="en">
<head>
<meta charset="utf-8">
<title>Radiant Gatherings Co. — Business Card</title>
<link rel="stylesheet" href="https://fonts.googleapis.com/css2?family=Open+Sans:wght@400&family=Pinyon+Script&display=swap">
<style>
  :root {
    --backdrop: #e4e1dc;
    --card-white: #ffffff;
    --card-dark: #231f20;
    --card-back: #1a1819;
    --accent-red: #c8161d;
    --accent-red-deep: #7a0d11;
    --ink: #1b1b1b;
    --ink-soft: #5a5a5a;
    --paper-text: #f2f2f2;
    --back-text: #d9d9d9;
    --back-rule: #8a8a8a;
    --social-blue: #3b5998;
    --social-red: #cb2027;
  }
  html, body {
    margin: 0;
    width: 1200px;
    height: 871px;
    overflow: hidden;
    background: var(--backdrop);
  }
  .card {
    position: absolute;
    width: 700px;
    height: 400px;
    overflow: hidden;
    box-shadow: 0 8px 24px rgba(0,0,0,0.25);
    font-family: "Open Sans", sans-serif;
  }

  /* Back side */
  .card-back {
    left: 40px;
    top: 22px;
    background: var(--card-back);
  }
  .back-brand {
    position: absolute;
    left: 0;
    right: 0;
    top: 130px;
    margin: 0;
    text-align: center;
    font-size: 50px;
    font-weight: 400;
    color: var(--back-text);
    white-space: nowrap;
  }
  .back-brand .brand-mark {
    width: 20px;
    height: 20px;
    margin-left: 14px;
  }
  .back-rule {
    position: absolute;
    left: 150px;
    right: 150px;
    height: 1px;
    background: var(--back-rule);
  }
  .back-rule.upper { top: 118px; }
  .back-rule.lower { top: 216px; }

  /* Front side */
  .card-front {
    left: 460px;
    top: 440px;
  }
  .card-background {
    position: absolute;
    inset: 0;
  }
  .brand-name {
    position: absolute;
    left: 42px;
    top: 48px;
    margin: 0;
    font-size: 25px;
    font-weight: 400;
    color: var(--ink-soft);
  }
  .brand-mark {
    display: inline-block;
    width: 12px;
    height: 12px;
    margin-left: 9px;
    border-radius: 50%;
    background: var(--accent-red);
    vertical-align: middle;
  }
  .person {
    position: absolute;
    right: 35px;
    top: 64px;
    text-align: right;
  }
  .person-name {
    margin: 0;
    font-size: 31px;
    font-weight: 400;
    color: var(--ink);
    line-height: 1.1;
  }
  .person-role {
    margin: 4px 0 0;
    font-size: 19px;
    color: var(--accent-red);
  }
  .tagline {
    position: absolute;
    right: 35px;
    top: 142px;
    margin: 0;
    font-family: "Pinyon Script", cursive;
    font-size: 25px;
    line-height: 1.05;
    text-align: right;
    color: var(--ink);
  }
  .contact-list {
    position: absolute;
    left: 40px;
    top: 208px;
    margin: 0;
    padding: 0;
    list-style: none;
  }
  .contact-item {
    display: flex;
    align-items: center;
    height: 36px;
    font-size: 18px;
    color: var(--paper-text);
  }
  .contact-icon {
    width: 18px;
    height: 18px;
    margin-right: 16px;
    flex: none;
  }
  .social-links {
    position: absolute;
    right: 28px;
    bottom: 24px;
    display: flex;
    gap: 7px;
  }
  .social-square {
    width: 28px;
    height: 28px;
    border-radius: 2px;
  }
  .social-square.network-one { background: var(--social-blue); }
  .social-square.network-two { background: var(--social-red); }
</style>
</head>
<body>
  <article class="card card-back">
    <span class="back-rule upper"></span>
    <h1 class="back-brand">Radiant Gatherings Co.<span class="brand-mark"></span></h1>
    <span class="back-rule lower"></span>
  </article>

  <article class="card card-front">
    <svg class="card-background" viewBox="0 0 700 400" preserveAspectRatio="none" aria-hidden="true">
      <rect width="700" height="400" fill="var(--card-dark)"/>
      <polygon points="0,0 700,0 700,228 0,179" fill="var(--card-white)"/>
      <polygon points="0,179 700,228 700,233 0,184" fill="var(--accent-red)"/>
      <polygon points="0,184 700,233 700,237 0,188" fill="var(--accent-red-deep)" opacity="0.6"/>
    </svg>

    <h2 class="brand-name">Radiant Gatherings Co.<span class="brand-mark"></span></h2>

    <div class="person">
      <h3 class="person-name">Delphine Marsh</h3>
      <p class="person-role">Event Manager / Owner</p>
    </div>

    <p class="tagline">Making each one of your gatherings<br>radiant...</p>

    <ul class="contact-list">
      <li class="contact-item">
        <svg class="contact-icon" viewBox="0 0 24 24" aria-hidden="true"><path fill="#f2f2f2" d="M6.6 2.5c.6-.3 1.2 0 1.5.5l1.7 3.2c.3.6.2 1.2-.3 1.6L8 9c1 2.4 2.8 4.3 5.1 5.4l1.2-1.5c.4-.5 1.1-.6 1.6-.3l3.2 1.8c.6.3.8 1 .5 1.6l-1 2.2c-.4.8-1.3 1.2-2.2 1C9.5 17.7 4.7 12.6 3.4 5.8c-.2-.9.3-1.8 1.1-2.2z"/></svg>
        0491 836 254
      </li>
      <li class="contact-item">
        <svg class="contact-icon" viewBox="0 0 24 24" aria-hidden="true"><rect x="2" y="5" width="20" height="14" rx="1.5" fill="#f2f2f2"/><path d="M2.5 6 12 13l9.5-7" fill="none" stroke="#231f20" stroke-width="1.6"/></svg>
        delphine@radiantgatheringsco.com.au
      </li>
      <li class="contact-item">
        <svg class="contact-icon" viewBox="0 0 24 24" aria-hidden="true"><g fill="none" stroke="#f2f2f2" stroke-width="1.6"><circle cx="12" cy="12" r="9.5"/><ellipse cx="12" cy="12" rx="4" ry="9.5"/><path d="M2.5 12h19M4 7h16M4 17h16"/></g></svg>
        www.radiantgatheringsco.com.au
      </li>
    </ul>

    <div class="social-links">
      <span class="social-square network-one"></span>
      <span class="social-square network-two"></span>
    </div>
  </article>
</body>
</html>
```